Turn this into a clear and concise

Attached is a screen shot that we currently show to investors from a software program. We need you to illustrate this in a much more professional looking and easy to view and understand way. If we like your style and attention to detail there is more work behind this.
Industry/Entity Type
Software

```html
<!DOCTYPE html>
<html lang="en">
<head>
<meta charset="utf-8">
<title>Sources – Intra-day Countertrend US Hours</title>
<link rel="stylesheet" href="https://fonts.googleapis.com/css2?family=Lato:wght@700&family=Open+Sans:wght@400&family=Carlito:ital,wght@0,700;1,400&family=Arimo:wght@400;700&display=swap">
<style>
  :root {
    --frame-black: #000000;
    --parchment-light: #ecd7a4;
    --parchment-mid: #e2c98f;
    --parchment-dark: #d6bb80;
    --title-green: #1f5a3c;
    --title-glow: #eef6ea;
    --ink: #1c1c1c;
    --bullet-blue: #3f77c4;
    --chart-green: #93c08a;
    --session-slate: #5f7a86;
    --axis-text: #111111;
    --axis-line: #3a3a3a;
    --candle-up: #e4f5dc;
    --candle-down: #c42424;
    --candle-line: #2e2e2e;
    --rsi-line: #1c6e1c;
    --rsi-upper: #f2e23a;
    --rsi-lower: #9c86c4;
    --volume-bar: #2a2ae0;
    --level-red: #d23a2a;
    --level-orange: #e39a2c;
    --level-blue: #5a5aa0;
    --page-number: #9a8a66;
  }
  html, body {
    margin: 0;
    width: 1200px;
    height: 704px;
    overflow: hidden;
    background: var(--frame-black);
  }
  .slide {
    position: absolute;
    left: 131px;
    top: 0;
    width: 938px;
    height: 704px;
    background: radial-gradient(ellipse at 50% 40%, var(--parchment-light) 0%, var(--parchment-mid) 60%, var(--parchment-dark) 100%);
  }
  .slide-title {
    position: absolute;
    left: 0;
    width: 938px;
    top: 14px;
    margin: 0;
    text-align: center;
    font-family: "Lato", sans-serif;
    font-weight: 700;
    font-size: 74px;
    line-height: 90px;
    letter-spacing: 1px;
    color: var(--title-green);
    text-shadow: 0 0 4px var(--title-glow), 0 0 8px var(--title-glow);
  }
  .bullet {
    position: absolute;
    left: 236px;
    top: 138px;
    margin: 0;
    font-family: "Open Sans", sans-serif;
    font-size: 25px;
    line-height: 36px;
    color: var(--ink);
    display: flex;
    align-items: center;
    gap: 14px;
  }
  .bullet svg { width: 16px; height: 16px; }
  .trade-caption {
    position: absolute;
    left: 91px;
    width: 739px;
    top: 230px;
    margin: 0;
    text-align: center;
    font-family: "Carlito", sans-serif;
    font-weight: 700;
    font-size: 17px;
    color: var(--ink);
  }
  .chart-label {
    position: absolute;
    top: 260px;
    margin: 0;
    font-family: "Carlito", sans-serif;
    font-style: italic;
    font-size: 17px;
    color: var(--ink);
  }
  .chart-label.entry { left: 217px; }
  .chart-label.exit { left: 616px; }
  .chart-strip {
    position: absolute;
    left: 91px;
    top: 290px;
    width: 739px;
    height: 366px;
    background: #ffffff;
  }
  .chart-panel {
    position: absolute;
    top: 0;
    height: 366px;
    background: var(--chart-green);
  }
  .chart-panel.entry { left: 0; width: 346px; }
  .chart-panel.exit { left: 386px; width: 352px; }
  .chart-panel svg { display: block; }
  .axis-text { font-family: "Arimo", sans-serif; font-size: 11px; font-weight: 700; fill: var(--axis-text); }
  .level-text { font-family: "Arimo", sans-serif; font-size: 10px; font-weight: 700; }
  .level-text.orange { fill: #8a4e00; }
  .level-text.blue { fill: var(--level-blue); }
  .pane-label { font-family: "Arimo", sans-serif; font-size: 12px; fill: var(--axis-text); }
  .pane-label.bold { font-weight: 700; font-size: 14px; }
  .page-number {
    position: absolute;
    right: 58px;
    bottom: 28px;
    font-family: "Open Sans", sans-serif;
    font-size: 11px;
    color: var(--page-number);
  }
</style>
</head>
<body>
<main class="slide">
  <h1 class="slide-title">Sources</h1>
  <p class="bullet">
    <svg viewBox="0 0 16 16" aria-hidden="true"><polygon points="2,2 14,8 2,14 6,8" fill="var(--bullet-blue)"/></svg>
    Intra-day Countertrend US Hours
  </p>
  <p class="trade-caption">Example Trade: 30 year Treasury Bond, 7/31/14 “Payroll Friday”</p>
  <p class="chart-label entry">Entry (Sell)</p>
  <p class="chart-label exit">Exit (Buy)</p>

  <div class="chart-strip">
    <div class="chart-panel entry">
      <svg width="346" height="366" viewBox="0 0 346 366" role="img" aria-label="Entry chart: price, RSI and volume, sell signal near 11am">
        <rect x="69" y="2" width="175" height="158" fill="var(--session-slate)"/>
        <line x1="0" y1="13" x2="283" y2="13" stroke="var(--level-red)" stroke-width="1.2"/>
        <g stroke="var(--level-orange)" stroke-width="1" stroke-dasharray="3 2">
          <line x1="0" y1="27" x2="283" y2="27"/>
          <line x1="0" y1="34" x2="283" y2="34"/>
          <line x1="0" y1="40" x2="283" y2="40"/>
          <line x1="0" y1="47" x2="283" y2="47"/>
          <line x1="0" y1="54" x2="283" y2="54"/>
        </g>
        <g id="candles" stroke="var(--candle-line)" stroke-width="1">
          <g>
            <line x1="12" y1="48" x2="12" y2="64"/><line x1="19.6" y1="58" x2="19.6" y2="64"/><line x1="27.2" y1="58" x2="27.2" y2="64"/><line x1="34.8" y1="57" x2="34.8" y2="63"/><line x1="42.4" y1="58" x2="42.4" y2="64"/><line x1="50" y1="59" x2="50" y2="65"/><line x1="57.6" y1="60" x2="57.6" y2="66"/><line x1="65.2" y1="61" x2="65.2" y2="70"/><line x1="72.8" y1="64" x2="72.8" y2="84"/><line x1="80.4" y1="78" x2="80.4" y2="96"/><line x1="88" y1="88" x2="88" y2="108"/><line x1="95.6" y1="100" x2="95.6" y2="128"/><line x1="103.2" y1="112" x2="103.2" y2="150"/><line x1="110.8" y1="110" x2="110.8" y2="132"/><line x1="118.4" y1="106" x2="118.4" y2="124"/><line x1="126" y1="108" x2="126" y2="118"/><line x1="133.6" y1="106" x2="133.6" y2="116"/><line x1="141.2" y1="105" x2="141.2" y2="114"/><line x1="148.8" y1="104" x2="148.8" y2="114"/><line x1="156.4" y1="104" x2="156.4" y2="112"/><line x1="164" y1="100" x2="164" y2="112"/><line x1="171.6" y1="92" x2="171.6" y2="110"/><line x1="179.2" y1="86" x2="179.2" y2="102"/><line x1="186.8" y1="82" x2="186.8" y2="98"/><line x1="194.4" y1="82" x2="194.4" y2="98"/><line x1="202" y1="88" x2="202" y2="110"/><line x1="209.6" y1="90" x2="209.6" y2="102"/><line x1="217.2" y1="88" x2="217.2" y2="100"/><line x1="224.8" y1="86" x2="224.8" y2="98"/><line x1="232.4" y1="82" x2="232.4" y2="96"/><line x1="240" y1="80" x2="240" y2="94"/><line x1="247.6" y1="76" x2="247.6" y2="90"/><line x1="255.2" y1="72" x2="255.2" y2="88"/><line x1="262.8" y1="74" x2="262.8" y2="84"/><line x1="270.4" y1="62" x2="270.4" y2="80"/><line x1="278" y1="54" x2="278" y2="72"/>
          </g>
          <g fill="var(--candle-down)">
            <rect x="9.5" y="52" width="5" height="10"/><rect x="62.7" y="63" width="5" height="5"/><rect x="70.3" y="66" width="5" height="14"/><rect x="77.9" y="80" width="5" height="12"/><rect x="85.5" y="90" width="5" height="14"/><rect x="93.1" y="104" width="5" height="16"/><rect x="100.7" y="118" width="5" height="12"/><rect x="146.3" y="106" width="5" height="6"/><rect x="191.9" y="86" width="5" height="8"/><rect x="199.5" y="92" width="5" height="10"/><rect x="252.7" y="76" width="5" height="8"/>
          </g>
          <g fill="var(--candle-up)">
            <rect x="17.1" y="60" width="5" height="2"/><rect x="24.7" y="60" width="5" height="2"/><rect x="32.3" y="59" width="5" height="2"/><rect x="39.9" y="60" width="5" height="2"/><rect x="47.5" y="61" width="5" height="2"/><rect x="55.1" y="62" width="5" height="2"/><rect x="108.3" y="114" width="5" height="10"/><rect x="115.9" y="110" width="5" height="8"/><rect x="123.5" y="110" width="5" height="4"/><rect x="131.1" y="108" width="5" height="4"/><rect x="138.7" y="108" width="5" height="3"/><rect x="153.9" y="107" width="5" height="3"/><rect x="161.5" y="104" width="5" height="4"/><rect x="169.1" y="96" width="5" height="10"/><rect x="176.7" y="90" width="5" height="10"/><rect x="184.3" y="86" width="5" height="10"/><rect x="207.1" y="94" width="5" height="4"/><rect x="214.7" y="92" width="5" height="4"/><rect x="222.3" y="90" width="5" height="4"/><rect x="229.9" y="86" width="5" height="6"/><rect x="237.5" y="84" width="5" height="6"/><rect x="245.1" y="80" width="5" height="6"/><rect x="260.3" y="78" width="5" height="2"/><rect x="267.9" y="66" width="5" height="10"/><rect x="275.5" y="58" width="5" height="10"/>
          </g>
        </g>
        <rect x="268.5" y="31" width="3" height="8" fill="var(--level-red)"/>
        <polygon points="266,39 274,39 270,46" fill="var(--level-red)"/>
        <line x1="283" y1="0" x2="283" y2="343" stroke="var(--axis-line)"/>
        <text class="axis-text" x="290" y="17">137'24</text>
        <text class="level-text orange" x="290" y="31">137'20</text>
        <text class="level-text orange" x="290" y="57">137'12</text>
        <text class="axis-text" x="290" y="72">137'08</text>
        <text class="axis-text" x="290" y="114">136'28</text>
        <text class="axis-text" x="290" y="150">136'16</text>
        <line x1="0" y1="160" x2="346" y2="160" stroke="var(--axis-line)"/>
        <line x1="0" y1="189" x2="283" y2="189" stroke="var(--rsi-upper)" stroke-width="2"/>
        <line x1="0" y1="244" x2="283" y2="244" stroke="var(--rsi-lower)" stroke-width="1.5"/>
        <polyline fill="none" stroke="var(--rsi-line)" stroke-width="1.6" points="10,230 18,246 30,246 40,232 50,238 60,244 75,256 90,261 103,262 110,236 120,232 130,222 140,228 150,206 160,202 168,192 176,184 182,182 190,196 198,203 206,190 214,182 222,196 232,204 242,192 250,190 258,188 264,200 270,190 278,188"/>
        <text class="pane-label bold" x="76" y="200">RSI</text>
        <text class="axis-text" x="296" y="176">100</text>
        <text class="axis-text" x="296" y="266">0</text>
        <line x1="0" y1="280" x2="346" y2="280" stroke="var(--axis-line)"/>
        <text class="pane-label" x="212" y="293">Volume</text>
        <text class="axis-text" x="290" y="293">20,000</text>
        <text class="axis-text" x="290" y="321">10,000</text>
        <g fill="var(--volume-bar)">
          <rect x="10" y="337" width="3" height="6"/><rect x="17.6" y="331" width="3" height="12"/><rect x="25.2" y="336" width="3" height="7"/><rect x="32.8" y="336" width="3" height="7"/><rect x="40.4" y="337" width="3" height="6"/><rect x="48" y="336" width="3" height="7"/><rect x="55.6" y="331" width="3" height="12"/><rect x="63.2" y="325" width="3" height="18"/><rect x="70.8" y="318" width="3" height="25"/><rect x="78.4" y="312" width="3" height="31"/><rect x="86" y="284" width="3" height="59"/><rect x="93.6" y="306" width="3" height="37"/><rect x="101.2" y="292" width="3" height="51"/><rect x="108.8" y="318" width="3" height="25"/><rect x="116.4" y="320" width="3" height="23"/><rect x="124" y="325" width="3" height="18"/><rect x="131.6" y="328" width="3" height="15"/><rect x="139.2" y="334" width="3" height="9"/><rect x="146.8" y="331" width="3" height="12"/><rect x="154.4" y="336" width="3" height="7"/><rect x="162" y="329" width="3" height="14"/><rect x="169.6" y="310" width="3" height="33"/><rect x="177.2" y="318" width="3" height="25"/><rect x="184.8" y="327" width="3" height="16"/><rect x="192.4" y="323" width="3" height="20"/><rect x="200" y="334" width="3" height="9"/><rect x="207.6" y="325" width="3" height="18"/><rect x="215.2" y="329" width="3" height="14"/><rect x="222.8" y="333" width="3" height="10"/><rect x="230.4" y="331" width="3" height="12"/><rect x="238" y="331" width="3" height="12"/><rect x="245.6" y="328" width="3" height="15"/><rect x="253.2" y="326" width="3" height="17"/><rect x="260.8" y="331" width="3" height="12"/><rect x="268.4" y="325" width="3" height="18"/><rect x="276" y="331" width="3" height="12"/>
        </g>
        <line x1="0" y1="343" x2="346" y2="343" stroke="var(--axis-line)"/>
        <text class="axis-text" x="34" y="358">8am</text>
        <text class="axis-text" x="113" y="358">9am</text>
        <text class="axis-text" x="191" y="358">10am</text>
        <text class="axis-text" x="262" y="358">11am</text>
      </svg>
    </div>

    <div class="chart-panel exit">
      <svg width="352" height="366" viewBox="0 0 352 366" role="img" aria-label="Exit chart: price, RSI and volume, buy signal after 11am">
        <rect x="51" y="2" width="179" height="158" fill="var(--session-slate)"/>
        <line x1="0" y1="40" x2="289" y2="40" stroke="var(--level-orange)" stroke-width="1.5" stroke-dasharray="3 2"/>
        <line x1="0" y1="61" x2="289" y2="61" stroke="var(--level-blue)" stroke-width="1" stroke-dasharray="2 2"/>
        <g transform="translate(-6,0) scale(0.97 1)">
          <use href="#candles"/>
        </g>
        <g stroke="var(--candle-line)" stroke-width="1">
          <line x1="265" y1="44" x2="265" y2="60"/><line x1="272" y1="46" x2="272" y2="56"/><line x1="279" y1="50" x2="279" y2="58"/><line x1="286" y1="52" x2="286" y2="58"/>
          <rect x="262.5" y="48" width="5" height="10" fill="var(--candle-up)"/>
          <rect x="269.5" y="50" width="5" height="3" fill="var(--candle-up)"/>
          <rect x="276.5" y="53" width="5" height="2" fill="var(--candle-up)"/>
          <rect x="283.5" y="54" width="4" height="2" fill="var(--candle-up)"/>
        </g>
        <rect x="255.5" y="29" width="3" height="8" fill="var(--level-red)"/>
        <polygon points="253,37 261,37 257,44" fill="var(--level-red)"/>
        <line x1="289" y1="0" x2="289" y2="343" stroke="var(--axis-line)"/>
        <text class="axis-text" x="296" y="17">137'24</text>
        <text class="level-text orange" x="296" y="44">137'16</text>
        <text class="level-text blue" x="296" y="64">137'10</text>
        <text class="axis-text" x="296" y="114">136'28</text>
        <text class="axis-text" x="296" y="150">136'16</text>
        <line x1="0" y1="160" x2="352" y2="160" stroke="var(--axis-line)"/>
        <line x1="0" y1="189" x2="289" y2="189" stroke="var(--rsi-upper)" stroke-width="2"/>
        <line x1="0" y1="240" x2="289" y2="240" stroke="var(--rsi-lower)" stroke-width="1.5"/>
        <polyline fill="none" stroke="var(--rsi-line)" stroke-width="1.6" points="10,244 18,244 28,232 38,236 46,244 56,248 70,254 86,254 96,230 106,226 116,214 126,222 136,204 146,196 154,190 162,182 170,200 178,206 186,194 194,198 202,204 212,190 222,182 230,200 238,196 246,188 256,182 264,180 274,190 282,196"/>
        <text class="pane-label bold" x="38" y="196">RSI</text>
        <text class="axis-text" x="302" y="176">100</text>
        <text class="axis-text" x="302" y="262">0</text>
        <line x1="0" y1="280" x2="352" y2="280" stroke="var(--axis-line)"/>
        <text class="pane-label" x="204" y="292">Volume</text>
        <text class="axis-text" x="296" y="293">20,000</text>
        <text class="axis-text" x="296" y="321">10,000</text>
        <g transform="translate(-6,0) scale(0.97 1)" fill="var(--volume-bar)">
          <rect x="10" y="337" width="3" height="6"/><rect x="17.6" y="336" width="3" height="7"/><rect x="25.2" y="336" width="3" height="7"/><rect x="32.8" y="337" width="3" height="6"/><rect x="40.4" y="336" width="3" height="7"/><rect x="48" y="333" width="3" height="10"/><rect x="55.6" y="325" width="3" height="18"/><rect x="63.2" y="318" width="3" height="25"/><rect x="70.8" y="284" width="3" height="59"/><rect x="78.4" y="296" width="3" height="47"/><rect x="86" y="288" width="3" height="55"/><rect x="93.6" y="306" width="3" height="37"/><rect x="101.2" y="316" width="3" height="27"/><rect x="108.8" y="322" width="3" height="21"/><rect x="116.4" y="328" width="3" height="15"/><rect x="124" y="333" width="3" height="10"/><rect x="131.6" y="331" width="3" height="12"/><rect x="139.2" y="336" width="3" height="7"/><rect x="146.8" y="329" width="3" height="14"/><rect x="154.4" y="330" width="3" height="13"/><rect x="162" y="312" width="3" height="31"/><rect x="169.6" y="322" width="3" height="21"/><rect x="177.2" y="328" width="3" height="15"/><rect x="184.8" y="323" width="3" height="20"/><rect x="192.4" y="334" width="3" height="9"/><rect x="200" y="325" width="3" height="18"/><rect x="207.6" y="329" width="3" height="14"/><rect x="215.2" y="330" width="3" height="13"/><rect x="222.8" y="331" width="3" height="12"/><rect x="230.4" y="326" width="3" height="17"/><rect x="238" y="331" width="3" height="12"/><rect x="245.6" y="326" width="3" height="17"/><rect x="253.2" y="320" width="3" height="23"/><rect x="260.8" y="322" width="3" height="21"/><rect x="268.4" y="331" width="3" height="12"/><rect x="276" y="334" width="3" height="9"/><rect x="283.6" y="333" width="3" height="10"/><rect x="291" y="335" width="3" height="8"/>
        </g>
        <line x1="0" y1="343" x2="352" y2="343" stroke="var(--axis-line)"/>
        <text class="axis-text" x="23" y="358">8am</text>
        <text class="axis-text" x="104" y="358">9am</text>
        <text class="axis-text" x="182" y="358">10am</text>
        <text class="axis-text" x="254" y="358">11am</text>
      </svg>
    </div>
  </div>

  <span class="page-number">1</span>
</main>
</body>
</html>
```